VELUNDORA Multistep design - needs to match our existing design.

We have a multistep form(7 pages) we need the design for (rest of the website is done).
The multistep form is a vital part of the website, as it is the main service - so the form design should fit into the rest of the site.
Please take a look at the attached file - all about colors, fonts etc. is included in the file.

Target Market(s)

People looking for an interior architect in Denmark

Industry/Entity Type

Interior Design

Number of Pages Required

1 page

Requirements
Nice to have
• It's attached in the pdf file

```html
<!DOCTYPE html>
<html lang="en">
<head>
<meta charset="utf-8">
<title>VELUNDORA – Private form</title>
<link href="https://fonts.googleapis.com/css2?family=Raleway:wght@400;500&display=swap" rel="stylesheet">
<style>
  :root {
    --page-bg: #f0f0f0;
    --nav-bg: #080808;
    --hero-dark: #111113;
    --hero-mid: #2a2a2c;
    --hero-warm: #3a3028;
    --text-main: #ffffff;
    --text-soft: #d6d6d6;
    --text-muted: #9a9a9a;
    --field-border: #8a8a8a;
    --field-bg: rgba(255, 255, 255, 0.06);
    --button-bg: #ffffff;
    --button-text: #111111;
  }
  * { box-sizing: border-box; margin: 0; padding: 0; }
  html, body {
    width: 1200px; height: 1200px; overflow: hidden;
    background: var(--page-bg);
    font-family: "Raleway", sans-serif;
  }
  .site {
    position: absolute; left: 61px; top: 114px;
    width: 1079px; height: 823px; overflow: hidden;
    background: var(--hero-dark);
  }
  .hero-photo {
    position: absolute; inset: 0;
    background:
      radial-gradient(ellipse at 30% 35%, rgba(90, 45, 45, 0.45), transparent 45%),
      radial-gradient(ellipse at 80% 30%, rgba(80, 65, 50, 0.45), transparent 40%),
      radial-gradient(ellipse at 35% 60%, rgba(95, 85, 60, 0.35), transparent 45%),
      linear-gradient(180deg, var(--hero-mid) 0%, var(--hero-warm) 50%, var(--hero-dark) 100%);
  }
  .site-nav {
    position: absolute; left: 0; top: 0; width: 100%; height: 56px;
    background: var(--nav-bg);
    display: flex; align-items: center; justify-content: space-between;
    padding: 0 34px;
  }
  .brand { color: var(--text-main); font-size: 22px; font-weight: 400; letter-spacing: 0.2px; }
  .nav-links { display: flex; gap: 29px; list-style: none; }
  .nav-links li { color: var(--text-main); font-size: 13px; }
  .content { position: absolute; left: 0; top: 0; width: 100%; }
  .page-title {
    position: absolute; top: 164px; width: 100%; text-align: center;
    color: var(--text-main); font-size: 26px; font-weight: 400;
  }
  .page-lead {
    position: absolute; top: 211px; width: 100%; text-align: center;
    color: var(--text-muted); font-size: 12px;
  }
  .form-title {
    position: absolute; top: 292px; width: 100%; text-align: center;
    color: var(--text-main); font-size: 18px; font-weight: 400;
  }
  .form-lead {
    position: absolute; top: 328px; width: 100%; text-align: center;
    color: var(--text-muted); font-size: 12px;
  }
  .request-form { position: absolute; left: 304px; top: 393px; width: 473px; }
  .field-row { display: flex; gap: 14px; margin-bottom: 16px; }
  .field-row.tight { margin-bottom: 15px; }
  .field {
    width: 229px; height: 35px;
    border: 1px solid var(--field-border); background: var(--field-bg);
    color: var(--text-soft); font-size: 12px;
    display: flex; align-items: center; padding-left: 10px;
  }
  .field.wide { width: 473px; }
  .type-question {
    display: flex; align-items: center; gap: 8px;
    color: var(--text-soft); font-size: 12px; margin-top: -4px;
  }
  .type-question .arrow { margin-right: 8px; }
  .choice { display: flex; align-items: center; gap: 6px; color: var(--text-main); font-size: 12px; }
  .choice.dim { color: var(--text-soft); }
  .choice + .choice { margin-left: 8px; }
  .features { display: flex; flex-wrap: wrap; column-gap: 14px; row-gap: 10px; margin-top: 18px; width: 480px; }
  .features .choice + .choice { margin-left: 0; }
  .box {
    width: 12px; height: 12px; border: 1px solid var(--text-soft); border-radius: 2px;
    display: inline-flex; align-items: center; justify-content: center;
  }
  .box.checked { background: var(--text-main); border-color: var(--text-main); }
  .dot {
    width: 12px; height: 12px; border: 1px solid var(--text-soft); border-radius: 50%;
    display: inline-flex; align-items: center; justify-content: center;
  }
  .dot.on::after { content: ""; width: 6px; height: 6px; border-radius: 50%; background: var(--text-main); }
  .continue {
    margin-top: 16px; width: 94px; height: 33px;
    background: var(--button-bg); color: var(--button-text);
    font-family: "Raleway", sans-serif; font-size: 13px; border: none;
  }
</style>
</head>
<body>
  <div class="site">
    <div class="hero-photo" role="img" aria-label="Dimmed photo of an architect's desk with a folding ruler and drawing papers"></div>

    <header class="site-nav">
      <div class="brand">VELUNDORA</div>
      <ul class="nav-links">
        <li>The concept</li>
        <li>Private</li>
        <li>profession</li>
        <li>Architect</li>
        <li>About VELUNDORA</li>
      </ul>
    </header>

    <main class="content">
      <h1 class="page-title">Private</h1>
      <p class="page-lead">There are many variations of passages of Lorem Ipsum</p>
      <h2 class="form-title">Fill in the form</h2>
      <p class="form-lead">There are many variations of passages of Lorem</p>

      <form class="request-form">
        <div class="field-row"><div class="field">First Name</div><div class="field">Last Name</div></div>
        <div class="field-row tight"><div class="field">Address</div><div class="field">Post code</div></div>
        <div class="field-row"><div class="field">Email</div><div class="field">Phone</div></div>
        <div class="field-row"><div class="field wide">Minimum Budget</div></div>

        <div class="type-question">
          <span>Is the case about a house or an apartment</span>
          <svg class="arrow" width="12" height="10" viewBox="0 0 12 10"><path d="M1 5h9M6.5 1.5L10 5l-3.5 3.5" stroke="#d6d6d6" stroke-width="1.1" fill="none"/></svg>
          <span class="choice"><span class="dot on"></span>HOUSE</span>
          <span class="choice dim"><span class="dot"></span>APARTMENT</span>
        </div>

        <div class="features">
          <span class="choice"><span class="box"></span>60's</span>
          <span class="choice"><span class="box"></span>70's</span>
          <span class="choice"><span class="box"></span>Architect Drawn</span>
          <span class="choice"><span class="box checked"><svg width="9" height="9" viewBox="0 0 9 9"><path d="M1.5 4.7l2 2 4-4.5" stroke="#111" stroke-width="1.5" fill="none"/></svg></span>Farm</span>
          <span class="choice"><span class="box"></span>Villa</span>
          <span class="choice"><span class="box"></span>Summerhouse</span>
          <span class="choice"><span class="box"></span>Standard house</span>
          <span class="choice"><span class="box"></span>Brick villa</span>
        </div>

        <button class="continue" type="button">Continue</button>
      </form>
    </main>
  </div>
</body>
</html>
```